skincare creams for tired moms

I need a package and a logo design for a skincare company based in California called Lumen Petal. I make day and night cream, under eye cream, and body lotion. The first product I plan to launch is an under eye cream. It does not have to be in these colors but I do teals, greens, black, and cobalt blue.

The package is going to either be in a box or a bag. Either way I go it will be like a gift box or bag. The design should make the person feel like they are getting something special and luxurious just for them.

I have small kids and it is really difficult to find a chunk of time to myself to update or review.

Target Market(s)

mainly first time moms. I am making an under eye cream that does not use retinol but is still powerful enough to get rid of bags and dark circles.

Industry/Entity Type

Cosmetics

Logo Text

The package and logo should incorporate the name Lumen Petal.

Font styles to use
Decorative
Script

Colors

Designer to choose colors to be used in the design.

Requirements
Nice to have
• maybe focus more on Petal instead of Lumen. Also incorporate plants or flowers
Should not have
• not a huge fan of pink

```html
<!DOCTYPE html>
<html lang="en">
<head>
<meta charset="utf-8">
<title>Lumen Petal — Eye Cream Label</title>
<link rel="stylesheet" href="https://fonts.googleapis.com/css2?family=Montserrat:wght@500;600&family=Oswald:wght@500&family=Fira+Sans:wght@400&display=swap">
<style>
  :root {
    --paper: #ffffff;
    --ink: #333333;
    --plum: #5e3a87;
    --plum-soft: #8a6bb0;
    --petal-tint: #efe9f5;
  }
  * { margin: 0; padding: 0; box-sizing: border-box; }
  html, body {
    width: 1124px;
    height: 1200px;
    overflow: hidden;
    background: var(--paper);
  }
  .label {
    position: relative;
    width: 1124px;
    height: 1200px;
    background: var(--paper);
  }
  .brand-dot {
    position: absolute;
    left: 532px;
    top: 250px;
    width: 60px;
    height: 60px;
    border-radius: 50%;
    background: var(--petal-tint);
  }
  .brand-name {
    position: absolute;
    top: 410px;
    left: 0;
    width: 1124px;
    text-align: center;
    font-family: "Montserrat", sans-serif;
    font-weight: 600;
    font-size: 38px;
    letter-spacing: 1px;
    color: var(--ink);
  }
  .brand-tagline {
    position: absolute;
    top: 468px;
    left: 0;
    width: 1124px;
    text-align: center;
    font-family: "Montserrat", sans-serif;
    font-weight: 500;
    font-size: 20px;
    letter-spacing: 10px;
    padding-left: 10px;
    color: var(--plum-soft);
  }
  .product-title {
    position: absolute;
    top: 612px;
    left: 378px;
    font-family: "Oswald", sans-serif;
    font-weight: 500;
    font-size: 100px;
    line-height: 96px;
    color: var(--plum);
    text-transform: uppercase;
  }
  .ingredients {
    position: absolute;
    top: 836px;
    left: 378px;
    list-style: none;
    font-family: "Fira Sans", sans-serif;
    font-size: 29px;
    line-height: 39px;
    color: var(--ink);
  }
  .ingredients li::before {
    content: "•";
    margin-right: 8px;
    font-size: 20px;
    vertical-align: middle;
  }
  .ingredients sup { font-size: 14px; }
  .divider {
    position: absolute;
    top: 1056px;
    left: 315px;
    width: 298px;
    height: 5px;
    background: var(--plum-soft);
  }
  .volume {
    position: absolute;
    top: 1088px;
    left: 378px;
    font-family: "Oswald", sans-serif;
    font-weight: 500;
    font-size: 34px;
    color: var(--ink);
    letter-spacing: 0.5px;
  }
</style>
</head>
<body>
  <main class="label">
    <span class="brand-dot" aria-hidden="true"></span>
    <h1 class="brand-name">LUMEN PETAL</h1>
    <p class="brand-tagline">BEAUTY</p>
    <h2 class="product-title">Eye<br>Cream</h2>
    <ul class="ingredients">
      <li>Peptilux-3000<sup>TM</sup></li>
      <li>Hylauronic acid</li>
      <li>Vitamin C</li>
      <li>Vitamin E</li>
      <li>Squalane</li>
    </ul>
    <div class="divider" aria-hidden="true"></div>
    <p class="volume">1.7 fl.oz / 50ml</p>
  </main>
</body>
</html>
```